Tallgrove Vale Management

I need a professional website. My current website is tallgrovevalemanagement.com and I hate it. It was created with some AI tool very quickly because I needed a site up and running with no advanced notice. I’m open to all designs .. I trust you, the professionals will deliver the results I’m anxiously awaiting! :)

```html
<!DOCTYPE html>
<html lang="en">
<head>
<meta charset="utf-8">
<title>Tallgrove Vale Management</title>
<link href="https://fonts.googleapis.com/css2?family=Poppins:wght@400;500;600;700&display=swap" rel="stylesheet">
<style>
:root{
  --navy:#1f3563;
  --navy-deep:#172a52;
  --navy-card:#1f3b75;
  --red:#8b1a2b;
  --ink:#2a2d3a;
  --muted:#555a66;
  --dark:#1a1e2c;
  --white:#ffffff;
  --line:#c9ccd3;
}
*{box-sizing:border-box;margin:0;padding:0}
html,body{width:1200px;height:4602px;overflow:hidden}
body{position:relative;font-family:'Poppins',sans-serif;color:var(--ink);background:var(--white)}
.abs{position:absolute}
.bands{position:absolute;left:0;top:0;width:1200px;height:4602px}
.btn{position:absolute;display:flex;align-items:center;justify-content:center;background:var(--red);color:var(--white);font-size:11px;font-weight:600;text-transform:uppercase;letter-spacing:.2px}
.h2{position:absolute;font-size:33px;font-weight:600;text-transform:uppercase;color:var(--ink)}
.h2.light{color:var(--white);width:1200px;left:0;text-align:center}
.photo{position:absolute}

/* header */
.topbar{position:absolute;left:300px;top:0;width:900px;height:36px;background:var(--navy-deep);clip-path:polygon(22px 0,100% 0,100% 100%,0 100%)}
.topbar .soc{position:absolute;top:11px;width:14px;height:14px;border-radius:50%;border:1.6px solid var(--white)}
.topbar .info{position:absolute;top:9px;font-size:12px;color:var(--white);display:flex;align-items:center;gap:8px}
.brand{position:absolute;left:40px;top:40px;display:flex;align-items:center;gap:8px;font-size:17px;font-weight:700;color:var(--navy);text-transform:uppercase;line-height:1.1}
.brand i{display:block;width:16px;height:16px;background:var(--red)}
.nav a{position:absolute;top:72px;font-size:13px;color:var(--ink);text-decoration:none}
.nav a.active{color:var(--red)}
.nav a.active::after{content:"";position:absolute;left:-8px;right:-8px;top:50px;height:3px;background:var(--red)}

/* hero */
.hero-title{position:absolute;left:159px;top:290px;font-size:39px;font-weight:500;line-height:48px;color:var(--white);text-transform:uppercase}
.hero-sub{position:absolute;left:161px;top:436px;font-size:13px;color:var(--white)}
.arrow-side{position:absolute;top:398px;width:14px;height:14px;border-top:2px solid var(--white);border-left:2px solid var(--white)}
.down{position:absolute;left:573px;top:612px;width:54px;height:54px;border-radius:50%;background:var(--white);box-shadow:0 2px 8px rgba(0,0,0,.25);display:flex;align-items:center;justify-content:center}

/* about */
.about p{position:absolute;left:161px;width:365px;font-size:13px;line-height:19.5px;color:var(--muted)}

/* services */
.card{position:absolute;top:1521px;width:277px;height:327px;background:var(--white)}
.card .img{position:absolute;left:0;top:0;width:277px;height:265px}
.card .label{position:absolute;left:16px;top:283px;font-size:13px;font-weight:600;text-transform:uppercase;color:var(--ink)}
.card .go{position:absolute;right:0;top:265px;width:60px;height:62px;background:var(--red);display:flex;align-items:center;justify-content:center}

/* how it works */
.step{position:absolute;left:623px;width:440px}
.step svg{position:absolute;left:0;top:4px}
.step h3{position:absolute;left:86px;top:0;font-size:15px;font-weight:600;text-transform:uppercase;color:var(--ink);white-space:nowrap}
.step p{position:absolute;left:86px;top:26px;width:340px;font-size:13px;line-height:19px;color:var(--muted)}

/* news */
.tile{position:absolute;width:277px}
.tile.navy{background:var(--navy-card);color:var(--white)}
.tile.plain{background:var(--white);color:var(--ink)}
.tile h4{font-size:13.5px;font-weight:600;text-transform:uppercase;text-align:center;line-height:18px;padding:0 20px}
.tile .date{display:flex;justify-content:center;align-items:center;gap:8px;font-size:13px;margin-top:12px}
.tile p{font-size:11px;line-height:14px;text-align:center;padding:0 40px;margin-top:10px;opacity:.9}
.tile .more{display:flex;justify-content:center;align-items:center;gap:6px;font-size:11px;font-weight:600;letter-spacing:1px;text-transform:uppercase;margin-top:12px}

/* contact */
.contact-card{position:absolute;left:161px;top:3733px;width:878px;height:518px;background:var(--white);box-shadow:0 4px 20px rgba(0,0,0,.12)}
.field{position:absolute;border:1px solid var(--line);font-size:12px;color:#6a6e78;padding:16px 15px}

/* footer */
.f-brand{position:absolute;left:0;width:1200px;top:4330px;display:flex;justify-content:center;align-items:center;gap:10px;font-size:22px;font-weight:700;color:var(--white);text-transform:uppercase}
.f-brand i{width:18px;height:18px;background:var(--red);display:block}
.f-nav a{position:absolute;top:4437px;font-size:12.5px;color:var(--white);text-decoration:none;text-transform:uppercase}
.f-info{position:absolute;top:4490px;display:flex;align-items:center;gap:10px;font-size:13px;color:var(--white)}
.f-info .dot{width:26px;height:26px;border-radius:50%;background:var(--red);display:flex;align-items:center;justify-content:center}
.f-soc{position:absolute;top:4567px;width:14px;height:14px;border-radius:50%;border:1.6px solid var(--white)}
</style>
</head>
<body>

<!-- background imagery and bands -->
<div class="photo" style="left:0;top:125px;width:1200px;height:680px;background:linear-gradient(120deg,#1d2f55 0%,#2e4f86 40%,#9a7b5a 70%,#c9a273 100%)" role="img" aria-label="Modern tiered residential tower with balconies at dusk"></div>
<div class="photo" style="left:0;top:1240px;width:1200px;height:900px;background:linear-gradient(180deg,#1f3563 0%,#24406f 50%,#1f3563 100%)" role="img" aria-label="Faint aerial view of a city skyline under a navy tint"></div>
<div class="photo" style="left:0;top:2680px;width:1200px;height:900px;background:linear-gradient(180deg,#1f3563,#243e6d 60%,#1f3563)" role="img" aria-label="Faint cityscape under a navy tint"></div>

<svg class="bands" viewBox="0 0 1200 4602" aria-hidden="true">
  <!-- hero bottom -->
  <polygon points="0,750 600,634 1200,700 1200,790 0,790" fill="var(--red)"/>
  <polygon points="0,786 600,662 1200,742 1200,1250 0,1250" fill="#fff"/>
  <!-- about to services -->
  <polygon points="0,1232 321,1366 1200,1250 1200,1260 0,1260" fill="#1f3563"/>
  <polygon points="0,1232 321,1350 321,1366 0,1262" fill="var(--red)"/>
  <!-- how it works -->
  <polygon points="0,2085 929,1980 1200,2107 1200,2125 0,2125" fill="var(--red)"/>
  <polygon points="0,2125 929,1995 1200,2110 1200,2680 321,2807 0,2680" fill="#f4f5f8"/>
  <polygon points="321,2807 1200,2680 1200,2706 321,2822" fill="var(--red)"/>
  <!-- contact band -->
  <polygon points="0,3600 768,3490 1200,3545 1200,3575 0,3635" fill="var(--red)"/>
  <polygon points="0,3630 768,3505 1200,3565 1200,3900 0,3985" fill="#eef0f4"/>
  <polygon points="0,3985 1200,3900 1200,4602 0,4602" fill="var(--dark)"/>
  <polygon points="0,3930 250,3950 0,3990" fill="var(--red)"/>
</svg>

<!-- header -->
<header>
  <div class="abs" style="left:0;top:0;width:1200px;height:125px;background:#fff"></div>
  <div class="topbar">
    <span class="soc" style="left:57px"></span>
    <span class="soc" style="left:95px"></span>
    <span class="soc" style="left:134px"></span>
    <span class="info" style="left:445px">
      <svg width="12" height="12" viewBox="0 0 24 24"><path d="M6.6 10.8a15 15 0 006.6 6.6l2.2-2.2c.3-.3.7-.4 1-.2 1.1.4 2.3.6 3.6.6.6 0 1 .4 1 1V20c0 .6-.4 1-1 1A17 17 0 013 4c0-.6.4-1 1-1h3.5c.6 0 1 .4 1 1 0 1.3.2 2.5.6 3.6.1.3 0 .7-.2 1z" fill="#fff"/></svg>555-014-2290</span>
    <span class="info" style="left:588px">
      <svg width="13" height="10" viewBox="0 0 26 20"><rect x="1" y="1" width="24" height="18" fill="none" stroke="#fff" stroke-width="2"/><path d="M1 1l12 10 12-10" fill="none" stroke="#fff" stroke-width="2"/></svg>info@tallgrovevalemanagement.com</span>
  </div>
  <div class="brand"><i></i><span>Tallgrove<br>Vale</span></div>
  <nav class="nav">
    <a class="active" style="left:330px">Home</a>
    <a style="left:416px">About Us</a>
    <a style="left:534px">Services</a>
    <a style="left:641px">How It Works</a>
    <a style="left:770px">News</a>
    <a style="left:848px">Contact Us</a>
  </nav>
  <div class="btn" style="left:979px;top:59px;width:160px;height:43px">Book Consultation</div>
</header>

<!-- hero -->
<section class="hero">
  <h1 class="hero-title">Professional Property<br>Management You<br>Can Trust</h1>
  <p class="hero-sub">A true partner, not just a vendor.</p>
  <div class="btn" style="left:161px;top:473px;width:189px;height:36px">Get A Free Consultation</div>
  <span class="arrow-side" style="left:32px;transform:rotate(-45deg)"></span>
  <span class="arrow-side" style="left:1154px;transform:rotate(135deg)"></span>
  <div class="down"><svg width="24" height="18" viewBox="0 0 24 18"><path d="M2 2l10 14L22 2M7 4l5 7 5-7" fill="none" stroke="var(--navy)" stroke-width="1.6"/></svg></div>
</section>

<!-- about -->
<section class="about">
  <div class="photo" style="left:527px;top:786px;width:673px;height:545px;background:linear-gradient(135deg,#ffffff 0%,#c8cdd8 45%,#3a4766 100%);clip-path:polygon(0 100%,20% 20%,75% 0,100% 5%,100% 88%,0 100%)" role="img" aria-label="Two smiling property managers in suits beside a glass office building"></div>
  <h2 class="h2" style="left:161px;top:838px">About Us</h2>
  <p style="top:896px">Our organization delivers comprehensive property management solutions that optimize asset performance and tenant satisfaction. By integrating advanced analytics with proven operational frameworks, our specialists ensure each property achieves sustained value appreciation.</p>
  <p style="top:1032px">Drawing on decades of collective expertise, the team facilitates regulatory compliance, cost efficiency, and proactive maintenance. This disciplined approach enables owners to preserve capital, enhance occupancy &nbsp;diverse market conditions.</p>
  <div class="btn" style="left:161px;top:1159px;width:137px;height:36px">Learn More</div>
</section>

<!-- services -->
<section class="services">
  <h2 class="h2 light" style="top:1428px">Our Services</h2>
  <div class="card" style="left:161px">
    <div class="img" style="background:linear-gradient(180deg,#bcc6cf,#5a5148 70%,#3d4a2f)" role="img" aria-label="Modern two-storey family home at dusk"></div>
    <span class="label">Residential Property</span>
    <span class="go"><svg width="22" height="10" viewBox="0 0 22 10"><path d="M0 5h20M15 1l5 4-5 4" fill="none" stroke="#fff" stroke-width="1.6"/></svg></span>
  </div>
  <div class="card" style="left:462px">
    <div class="img" style="background:linear-gradient(180deg,#9ec7ea,#3f6f9c 55%,#4c7a3a)" role="img" aria-label="Glass commercial office towers against a blue sky"></div>
    <span class="label">Commercial Property</span>
    <span class="go"><svg width="22" height="10" viewBox="0 0 22 10"><path d="M0 5h20M15 1l5 4-5 4" fill="none" stroke="#fff" stroke-width="1.6"/></svg></span>
  </div>
  <div class="card" style="left:762px">
    <div class="img" style="background:linear-gradient(90deg,#d9dde2,#f2f2f0 50%,#4d4f55)" role="img" aria-label="Agent handing house keys to a smiling couple"></div>
    <span class="label">Tenant Placement</span>
    <span class="go"><svg width="22" height="10" viewBox="0 0 22 10"><path d="M0 5h20M15 1l5 4-5 4" fill="none" stroke="#fff" stroke-width="1.6"/></svg></span>
  </div>
  <div class="btn" style="left:514px;top:1893px;width:170px;height:37px">View More Services</div>
</section>

<!-- how it works -->
<section class="how">
  <div class="photo" style="left:0;top:2179px;width:568px;height:527px;background:linear-gradient(135deg,#d8b7c0,#f1f1f3 45%,#9aa0aa);clip-path:polygon(45% 0,100% 78%,78% 78%,72% 100%,0 48%,0 20%)" role="img" aria-label="Man in a white shirt working on a laptop at an office desk"></div>
  <h2 class="h2" style="left:623px;top:2156px">How It Works</h2>
  <div class="step" style="top:2229px">
    <svg width="68" height="58" viewBox="0 0 68 58"><polygon points="34,0 68,58 0,58" fill="var(--navy)"/><path d="M29 30c2 5 5 8 10 10l2-2 4 2-2 4c-8 0-16-8-16-16l4-2 2 4z" fill="#fff"/></svg>
    <h3>Schedule A Consultation</h3>
    <p>Lorem Ipsum is simply dummy text of the printing and typesetting industry.</p>
  </div>
  <div class="step" style="top:2335px">
    <svg width="68" height="58" viewBox="0 0 68 58"><polygon points="34,0 68,58 0,58" fill="var(--navy)"/><path d="M34 26l10 9h-3v9h-5v-6h-4v6h-5v-9h-3z" fill="#fff"/></svg>
    <h3>Property Assessment</h3>
    <p>Lorem Ipsum is simply dummy text of the printing and typesetting industry.</p>
  </div>
  <div class="step" style="top:2441px">
    <svg width="68" height="58" viewBox="0 0 68 58"><polygon points="34,0 68,58 0,58" fill="var(--navy)"/><rect x="28" y="28" width="12" height="16" fill="none" stroke="#fff" stroke-width="2"/><path d="M31 33h6M31 37h6M31 41h6" stroke="#fff" stroke-width="1.5"/></svg>
    <h3>Tenant &amp; Property Management</h3>
    <p>Lorem Ipsum is simply dummy text of the printing and typesetting industry.</p>
  </div>
  <div class="step" style="top:2542px">
    <svg width="68" height="58" viewBox="0 0 68 58"><polygon points="34,0 68,58 0,58" fill="var(--navy)"/><circle cx="34" cy="33" r="5" fill="#fff"/><path d="M25 46c0-5 4-8 9-8s9 3 9 8z" fill="#fff"/></svg>
    <h3>Reports &amp; Support</h3>
    <p>Lorem Ipsum is simply dummy text of the printing and typesetting industry.</p>
  </div>
</section>

<!-- news -->
<section class="news">
  <h2 class="h2 light" style="top:2870px">Latest News</h2>

  <div class="tile photo" style="left:184px;top:2965px;height:218px;background:linear-gradient(135deg,#5b6a52,#d8d9d6 50%,#3b4a36)" role="img" aria-label="Two business people shaking hands outdoors"></div>
  <div class="tile navy" style="left:184px;top:3183px;height:189px;padding-top:24px">
    <h4>How To Maximize Your Rental Property Income</h4>
    <div class="date"><svg width="18" height="16" viewBox="0 0 18 16"><rect x="1" y="2" width="16" height="13" fill="none" stroke="#fff" stroke-width="1.6"/><path d="M1 6h16M5 9h2M9 9h2M13 9h2M5 12h2M9 12h2" stroke="#fff" stroke-width="1.6"/></svg>Feb 10,2026</div>
    <p>It is a long established fact that a reader will be distracted by th looking at its layout.</p>
    <div class="more">Learn More <svg width="12" height="8" viewBox="0 0 12 8"><path d="M0 4h10M7 1l3 3-3 3" fill="none" stroke="#fff" stroke-width="1.4"/></svg></div>
  </div>

  <div class="tile plain" style="left:462px;top:2965px;height:218px;padding-top:34px">
    <h4>5 Tips For Choosing The Right Property Management</h4>
    <div class="date"><svg width="18" height="16" viewBox="0 0 18 16"><rect x="1" y="2" width="16" height="13" fill="none" stroke="var(--red)" stroke-width="1.6"/><path d="M1 6h16M5 9h2M9 9h2M13 9h2M5 12h2M9 12h2" stroke="var(--red)" stroke-width="1.6"/></svg>Feb 10,2026</div>
    <p style="color:var(--muted)">It is a long established fact that a reader will be distracted by th looking at its layout.</p>
    <div class="more">Learn More <svg width="12" height="8" viewBox="0 0 12 8"><path d="M0 4h10M7 1l3 3-3 3" fill="none" stroke="var(--red)" stroke-width="1.4"/></svg></div>
  </div>
  <div class="tile photo" style="left:462px;top:3183px;height:189px;background:linear-gradient(135deg,#e0a24a,#8a5a32 50%,#3c5a2a)" role="img" aria-label="Miniature house model on a wooden table with a sunny backdrop"></div>

  <div class="tile photo" style="left:739px;top:2965px;height:218px;background:linear-gradient(180deg,#9fcbee,#cfd2d0 50%,#567a46)" role="img" aria-label="Modern apartment building with balconies and trees"></div>
  <div class="tile navy" style="left:739px;top:3183px;height:189px;padding-top:24px">
    <h4>Essential Property Maintenance Checklist</h4>
    <div class="date"><svg width="18" height="16" viewBox="0 0 18 16"><rect x="1" y="2" width="16" height="13" fill="none" stroke="#fff" stroke-width="1.6"/><path d="M1 6h16M5 9h2M9 9h2M13 9h2M5 12h2M9 12h2" stroke="#fff" stroke-width="1.6"/></svg>Feb 10,2026</div>
    <p>It is a long established fact that a reader will be distracted by th looking at its layout.</p>
    <div class="more">Learn More <svg width="12" height="8" viewBox="0 0 12 8"><path d="M0 4h10M7 1l3 3-3 3" fill="none" stroke="#fff" stroke-width="1.4"/></svg></div>
  </div>

  <div class="btn" style="left:514px;top:3427px;width:170px;height:37px">View All News</div>
</section>

<!-- contact -->
<section class="contact">
  <div class="contact-card">
    <h2 class="h2" style="left:0;width:878px;text-align:center;top:50px">Contact Us</h2>
    <div class="field" style="left:53px;top:130px;width:374px;height:50px">First Name</div>
    <div class="field" style="left:448px;top:130px;width:374px;height:50px">Last Name</div>
    <div class="field" style="left:53px;top:199px;width:374px;height:50px">Email Address</div>
    <div class="field" style="left:448px;top:199px;width:374px;height:50px">Phone Number</div>
    <div class="field" style="left:53px;top:268px;width:769px;height:146px">Message</div>
    <div class="btn" style="left:353px;top:450px;width:170px;height:35px">Submit</div>
  </div>
</section>

<!-- footer -->
<footer>
  <div class="f-brand"><i></i>Tallgrove Vale</div>
  <nav class="f-nav">
    <a style="left:343px">Home</a>
    <a style="left:436px">About Us</a>
    <a style="left:558px">Services</a>
    <a style="left:676px">News</a>
    <a style="left:771px">Contact Us</a>
  </nav>
  <div class="f-info" style="left:248px"><span class="dot"><svg width="12" height="12" viewBox="0 0 24 24"><path d="M6.6 10.8a15 15 0 006.6 6.6l2.2-2.2c.3-.3.7-.4 1-.2 1.1.4 2.3.6 3.6.6.6 0 1 .4 1 1V20c0 .6-.4 1-1 1A17 17 0 013 4c0-.6.4-1 1-1h3.5c.6 0 1 .4 1 1 0 1.3.2 2.5.6 3.6.1.3 0 .7-.2 1z" fill="#fff"/></svg></span>555-014-2290</div>
  <div class="f-info" style="left:436px"><span class="dot"><svg width="13" height="10" viewBox="0 0 26 20"><rect x="1" y="1" width="24" height="18" fill="none" stroke="#fff" stroke-width="2.4"/><path d="M1 1l12 10 12-10" fill="none" stroke="#fff" stroke-width="2.4"/></svg></span>info@tallgrovevalemanagement.com</div>
  <div class="f-info" style="left:764px"><span class="dot"><svg width="10" height="13" viewBox="0 0 20 26"><path d="M10 0a10 10 0 0110 10c0 7-10 16-10 16S0 17 0 10A10 10 0 0110 0z" fill="#fff"/><circle cx="10" cy="10" r="4" fill="var(--red)"/></svg></span>122, Lorem ipsum dolrd</div>
  <div class="abs" style="left:223px;top:4532px;width:754px;height:1px;background:rgba(255,255,255,.25)"></div>
  <span class="f-soc" style="left:548px"></span>
  <span class="f-soc" style="left:591px"></span>
  <span class="f-soc" style="left:634px"></span>
</footer>

</body>
</html>
```